Buch-/E-Book-Cover Existenzgründer und Gründungsinteressierte
Zielgruppe
Es geht um eine Buchcover mit dem Titel 'Wolkenhafen erkunden'; Zielgruppe sind Existenzgründer und Gründungsinteressierte
Aufgabenstellung
Das Buchcover sollte modern und frisch gestaltet werden, eine grobe Skizze ist beigefügt, unten rechts soll das Verlagslogo (klein) platziert werden
Haupttext „Wolkenhafen erkunden“ soll auffallend, vielleicht als Wortmarke, gestaltet werden – er sollte einen Wiedererkennungswert haben
Auf der Frontseite des Covers sollten auch die Schlüsselwörter zu den Hauptkapiteln integriert werden (siehe Idee Skizze), damit der Leser auf den 1. Blick einen Eindruck über die Inhalte des Ratgebers gewinnt
Format: Das Taschenbuch soll im Hochformat (13,97 cm x 21,59 cm, Bindung links, Veltrano Quill Print Service) erscheinen und das Buch hat ca. 190 Seiten. Das Cover soll ein Softcover (235g Chromokarton), 4/4 farbig sein.

```html
<!DOCTYPE html>
<html lang="de">
<head>
<meta charset="utf-8">
<title>Wolkenhafen erkunden – Buchcover</title>
<link href="https://fonts.googleapis.com/css2?family=Oswald:wght@500&family=Poppins:wght@700&family=Jost:wght@400&family=Lato:wght@400;700&display=swap" rel="stylesheet">
<style>
  :root {
    --backdrop: #555555;
    --paper: #f3f2f3;
    --olive: #4b5e2a;
    --olive-line: #6b7a45;
    --salmon: #ec9270;
    --ink: #454545;
    --badge: #7cc142;
    --white: #ffffff;
  }
  html, body {
    margin: 0;
    padding: 0;
    width: 1166px;
    height: 1200px;
    overflow: hidden;
    background: var(--backdrop);
  }
  .cover {
    position: absolute;
    left: 245px;
    top: 77px;
    width: 676px;
    height: 1046px;
    background: var(--paper);
    overflow: hidden;
  }
  .cover-photo {
    position: absolute;
    left: 0; top: 0;
    width: 676px;
    height: 525px;
    background:
      radial-gradient(ellipse at 75% 40%, #e2c6ad 0%, rgba(226,198,173,0) 40%),
      linear-gradient(180deg, #dfe3e0 0%, #c9c9c4 35%, #8f8983 65%, #6b635c 100%);
  }
  .bonus-badge {
    position: absolute;
    left: 72px; top: 370px;
    width: 168px; height: 168px;
    border-radius: 50%;
    background: var(--badge);
    color: var(--white);
    font-family: "Oswald", sans-serif;
    font-weight: 500;
    font-size: 22px;
    line-height: 1.2;
    text-align: center;
    display: flex;
    align-items: center;
    justify-content: center;
  }
  .bonus-badge span { transform: rotate(-14deg); display: block; }
  .title-main {
    position: absolute;
    left: 0; right: 0; top: 530px;
    margin: 0;
    text-align: center;
    font-family: "Oswald", sans-serif;
    font-weight: 500;
    font-size: 106px;
    line-height: 1.1;
    letter-spacing: -1px;
    color: var(--olive);
    white-space: nowrap;
  }
  .title-sub {
    position: absolute;
    left: 0; right: 0; top: 640px;
    margin: 0;
    text-align: center;
    font-family: "Poppins", sans-serif;
    font-weight: 700;
    font-size: 96px;
    line-height: 1;
    letter-spacing: -3px;
    color: var(--salmon);
    white-space: nowrap;
  }
  .subtitle {
    position: absolute;
    left: 0; right: 0; top: 739px;
    margin: 0;
    text-align: center;
    font-family: "Jost", sans-serif;
    font-weight: 400;
    font-size: 32px;
    line-height: 36px;
    color: var(--ink);
  }
  .topics-head {
    position: absolute;
    left: 50px; right: 57px; top: 823px;
    display: flex;
    align-items: center;
    gap: 14px;
    font-family: "Lato", sans-serif;
    font-weight: 700;
    font-size: 19px;
    color: var(--olive);
  }
  .topics-head::before, .topics-head::after {
    content: "";
    flex: 1;
    height: 1px;
    background: var(--olive-line);
  }
  .topics {
    position: absolute;
    left: 0; right: 0; top: 852px;
    margin: 0; padding: 0;
    list-style: none;
    text-align: center;
    font-family: "Lato", sans-serif;
    font-size: 19px;
    line-height: 29px;
    color: var(--ink);
  }
  .topics .tick { color: var(--olive); margin-right: 4px; }
  .author {
    position: absolute;
    left: 0; right: 0; top: 980px;
    margin: 0;
    text-align: center;
    font-family: "Lato", sans-serif;
    font-weight: 700;
    font-size: 34px;
    letter-spacing: 1px;
    color: var(--ink);
  }
  .publisher {
    position: absolute;
    left: 574px; top: 940px;
    width: 90px;
    display: flex;
    flex-direction: column;
    align-items: center;
    gap: 6px;
    font-family: "Lato", sans-serif;
    font-weight: 700;
    font-size: 15px;
    line-height: 17px;
    text-align: center;
    color: var(--ink);
  }
  .publisher-mark { width: 18px; height: 18px; background: var(--salmon); }
</style>
</head>
<body>
  <main class="cover">
    <div class="cover-photo" role="img" aria-label="Foto: lächelnde Café-Inhaberin mit Schürze vor einer Espressomaschine, im Hintergrund zwei Gäste mit Kaffee und Laptop"></div>
    <div class="bonus-badge"><span>BONUS:<br>Online-Trainings<br>und Vorlagen</span></div>

    <h1 class="title-main">WOLKENHAFEN</h1>
    <p class="title-sub">erkunden</p>
    <p class="subtitle">EXISTENZGRÜNDUNG FÜR<br>KLEINUNTERNEHMEN</p>

    <div class="topics-head">ALLES ÜBER</div>
    <ul class="topics">
      <li><span class="tick">✓</span>Behördengänge &nbsp;<span class="tick">✓</span>Rechtsform &nbsp;<span class="tick">✓</span>(digitale) Büroorganisation</li>
      <li><span class="tick">✓</span>Buchhaltung und Steuern <span class="tick">✓</span>Finanzierung und Fördermittel</li>
      <li><span class="tick">✓</span>Businessplan &nbsp;&nbsp;<span class="tick">✓</span>Versicherungen</li>
    </ul>

    <p class="author">Matthias Kerber</p>

    <div class="publisher">
      <span class="publisher-mark"></span>
      <span>Lindgrün Verlag</span>
    </div>
  </main>
</body>
</html>
```